Flyer for American Indian Elders on Dementia Warning Signs

We need a flyer designed for older adults who are American Indian or Alaska Native (in the U.S.).

Ideally, the flyer should complement the colors of our logos. The project logo and our organization logo are attached to the brief.

When people see the flyer we want them to feel that it represents their culture, is warm, and professional but relatable to older adults and people who have limited incomes.

I have attached an earlier draft of the document we designed ourselves BUT we want different and better.

It is for older adults who have trouble reading so:
1. you must use a font that is 11.5 points or larger
2. Do not put text over complex pictures or use shading with words
3. You can use a serif font for the heading, but should use san serif for the body text
4. There should be good contrast between the font color and background

Please do not use any images that include a head dress or pictures of American Indian people or things that are very traditional or "token" imagery.

We need to save a small space under the call out box/ somewhere on the flyer for other people to add their logo once they download.

Let us know if you have questions or need additional information.

Target Market(s)

Older American Indian people

Font styles to use
Serif
Sans Serif

Requirements
Must have
• Easy to read for older adults
Should not have
• indian headdress

```html
<!DOCTYPE html>
<html lang="en">
<head>
<meta charset="utf-8">
<title>10 Signs of Thinking or Memory Changes</title>
<link rel="stylesheet" href="https://fonts.googleapis.com/css2?family=Libre+Baskerville:wght@400&family=Raleway:wght@400;600&display=swap">
<style>
:root{
  --wine:#7c2a30;
  --wine-dark:#6a2228;
  --coral:#b9554f;
  --teal:#4aa6ad;
  --teal-dark:#2d6f77;
  --heading:#7a1f2a;
  --ink:#2b2b2b;
  --paper:#ffffff;
}
*{box-sizing:border-box;margin:0;padding:0}
html,body{width:950px;height:1200px;overflow:hidden;background:var(--paper)}
body{font-family:"Raleway",sans-serif;color:var(--ink)}
.flyer{position:relative;width:950px;height:1200px;background:var(--paper)}
.band{position:absolute;left:0;width:950px;height:30px;background:linear-gradient(90deg,var(--teal),var(--coral),var(--teal),var(--coral))}
.band--top{top:0}
.band--bottom{bottom:0}
.sidebar{position:absolute;left:0;top:33px;width:473px}
.title-block{height:194px;background:linear-gradient(135deg,var(--wine),var(--wine-dark));padding:16px 30px 0;display:flex;align-items:flex-start}
.title-block h1{font-family:"Libre Baskerville",serif;font-weight:400;color:#fff;font-size:25px;line-height:40px;letter-spacing:.3px}
.intro{height:217px;background:var(--coral);color:#fff;padding:16px 32px 0;font-size:15px;line-height:19px;text-align:justify}
.intro p+p{margin-top:18px}
.photo-grid{margin-top:13px;display:grid;grid-template-columns:1fr 1fr;grid-template-rows:130px 131px;gap:2px;height:263px}
.photo{display:block}
.photo--warm{background:linear-gradient(135deg,#c9625b,#8e3a3c)}
.photo--cool{background:linear-gradient(135deg,#3f8f98,#1f5960)}
.key-points{height:427px;background:var(--teal);color:#fff;padding:18px 22px 0;font-weight:600;font-size:16.5px;line-height:21px}
.key-points p+p{margin-top:20px}
.callout{position:absolute;left:37px;top:999px;width:401px;height:130px;background:linear-gradient(90deg,var(--coral),var(--wine-dark));color:#fff;text-align:center;padding:14px 20px 0;font-size:15px;line-height:19px}
.callout .url{font-weight:600;font-size:16.5px;margin-top:9px;line-height:27px}
.signs{position:absolute;left:491px;top:44px;width:440px;list-style:none;font-size:15.5px;line-height:20px}
.sign{margin-bottom:17px;padding-left:28px;position:relative}
.sign .num{position:absolute;left:0;top:0;font-weight:600;color:var(--heading)}
.sign h2{font-size:16.5px;font-weight:600;color:var(--heading);line-height:21px}
.sign h2 span{font-weight:400;color:var(--ink)}
.sign ul{list-style:none;margin-top:4px}
.sign li{position:relative;padding-left:14px;margin-bottom:5px}
.sign li::before{content:"";position:absolute;left:2px;top:9px;width:4px;height:4px;border-radius:50%;background:var(--teal)}
.sign p{margin-top:5px}
.sign p.lead{margin-top:0}
.partners{position:absolute;left:520px;top:1108px;width:410px;display:flex;justify-content:space-between;align-items:center}
.partner{display:flex;align-items:center;gap:8px;font-weight:600;color:var(--teal-dark);font-size:15px;line-height:17px}
.partner-mark{width:42px;height:42px;border-radius:50%;background:var(--teal)}
.partner-mark--square{border-radius:0;background:var(--wine)}
</style>
</head>
<body>
<main class="flyer">
  <div class="band band--top" role="img" aria-label="Chevron border pattern in teal and coral"></div>

  <aside class="sidebar">
    <header class="title-block">
      <h1>10 SIGNS OF THINKING OR MEMORY CHANGES THAT MIGHT BE DEMENTIA</h1>
    </header>
    <section class="intro">
      <p>As we get older, we may slow down a bit. This is a normal part of aging. Changes in memory or thinking that make it harder to get through the day, are not a normal part of aging. These may be early signs of dementia.</p>
      <p>Because American Indian and Alaska Native people have a high risk of dementia, it is important to know the warning signs. Do you have any of these 10 signs? If so, talk to your doctor.</p>
    </section>
    <div class="photo-grid">
      <div class="photo photo--warm" role="img" aria-label="Wooden signpost by a lake reading values, vision, mission, tinted red"></div>
      <div class="photo photo--cool" role="img" aria-label="Portrait of an elder in a wide-brim hat, tinted teal"></div>
      <div class="photo photo--cool" role="img" aria-label="Group of veterans at a gathering, tinted teal"></div>
      <div class="photo photo--warm" role="img" aria-label="Community dance gathering, tinted red"></div>
    </div>
    <section class="key-points">
      <p>American Indian and Alaska Native people have a high risk of dementia.</p>
      <p>Big changes in memory or thinking that make it hard to get through the day are not a normal part of aging.</p>
      <p>People with one or more of these 10 signs should talk to their doctor to find the cause. It is not always dementia.</p>
      <p>Early dementia diagnosis gives you a chance to get care and plan your future.</p>
    </section>
  </aside>

  <div class="callout">
    <p>To learn more about the warning signs of dementia in American Indian and Alaska Native people, visit:</p>
    <p class="url">www.northskybrainhealth.org<br>www.elderwellness.org/aging</p>
  </div>

  <ol class="signs">
    <li class="sign"><span class="num">1.</span><h2>Memory loss that affects your daily life.</h2><p class="lead">You may:</p>
      <ul><li>Forget events or important dates</li><li>Repeat yourself</li><li>Rely more often on lists or sticky notes to remember things</li></ul></li>
    <li class="sign"><span class="num">2.</span><h2>Trouble planning or solving problems.</h2><p class="lead">You may have a harder time:</p>
      <ul><li>Paying bills</li><li>Cooking recipes you have used for years</li></ul></li>
    <li class="sign"><span class="num">3.</span><h2>Get confused about the time, date, or where you are.</h2></li>
    <li class="sign"><span class="num">4.</span><h2>Daily tasks are getting harder, including:</h2>
      <ul><li>Driving</li><li>Making a grocery list or going shopping</li></ul></li>
    <li class="sign"><span class="num">5.</span><h2>Trouble with how your eyesight and thinking work together that gets worse. <span>This includes:</span></h2>
      <ul><li>Tripping, falls, or problems with your balance</li><li>Spilling or dropping things more</li></ul></li>
    <li class="sign"><span class="num">6.</span><h2>New trouble talking or writing.</h2>
      <p>You have a hard time finding the words you want to say. For example, you may say “that thing on your wrist that tells time” instead of “watch.”</p></li>
    <li class="sign"><span class="num">7.</span><h2>Lose and cannot find things. For example, you:</h2>
      <ul><li>Can’t find the coffee pot that you use every day</li><li>Might put your car keys in the freezer</li></ul></li>
    <li class="sign"><span class="num">8.</span><h2>Notice changes in mood or personality, such as being:</h2>
      <ul><li>Easily mad or sad in everyday situations</li><li>More fearful (scared) or suspicious (not trusting)</li></ul></li>
    <li class="sign"><span class="num">9.</span><h2>Act different and make poor choices.</h2><p class="lead">This may make you more likely to:</p>
      <ul><li>Spend money you do not have or be a scam victim</li><li>Stop washing up regularly or pay less attention to how you look</li><li>Forget to take care of your pet</li></ul></li>
    <li class="sign"><span class="num">10.</span><h2>Pull away from friends and family because it is harder to keep up.</h2>
      <p>You may not want to do things you used to enjoy, like sporting events, church, music, or sex.</p></li>
  </ol>

  <div class="partners">
    <div class="partner"><span class="partner-mark"></span><span>Northern Sky<br>Brain Health Center</span></div>
    <div class="partner"><span class="partner-mark partner-mark--square"></span><span>Council for<br>Elder Wellness</span></div>
  </div>

  <div class="band band--bottom" role="img" aria-label="Chevron border pattern in teal and coral"></div>
</main>
</body>
</html>
```